Engineering Consultant Business Card

I'm starting a new business as a high-end engineering consultant in a niche field. I've attached the jpg for my logo plus the branding guideline document that I've been following. You can see my business website here: www.tarvikworks.com
I'd like a business card that has the logo on one side, then the other side has (in any order): Tarvik Works, Inc.
Dana Whitlock
President and Chief EMC Engineer
www.tarvikworks.com
dana@tarvikworks.com
Optional: motto "We will solve your EMC problems as early as possible—ideally before they even start."
I'm not planning on including a phone number
Target Market(s)
Businesses, especially makers of electronics hardware
Industry/Entity Type
Electrical engineering
Contact Information for Business Card
Company name, my name, website, email

```html
<!DOCTYPE html>
<html lang="en">
<head>
<meta charset="UTF-8">
<title>Tarvik Works – Business Card</title>
<link href="https://fonts.googleapis.com/css2?family=Montserrat:wght@500;600;700&display=swap" rel="stylesheet">
<style>
  :root {
    --backdrop: #3b3c3f;
    --brand-blue: #2e4596;
    --accent-aqua: #7fcad6;
    --card-white: #ffffff;
    --ink-dark: #2a2a2e;
  }
  * { margin: 0; padding: 0; box-sizing: border-box; }
  html, body {
    width: 1200px; height: 1200px; overflow: hidden;
    background: var(--backdrop);
    font-family: "Montserrat", sans-serif;
  }
  .stage {
    width: 1200px; height: 1200px;
    display: flex; flex-direction: column; align-items: center; justify-content: center;
    gap: 44px;
  }
  .card {
    position: relative;
    width: 900px; height: 514px;
    border-radius: 40px;
    overflow: hidden;
    box-shadow: 0 14px 30px rgba(0,0,0,0.45);
  }
  .card-front { background: var(--card-white); }
  .card-back { background: var(--brand-blue); display: flex; align-items: center; justify-content: center; }

  .front-footer-stripe {
    position: absolute; left: 0; right: 0; bottom: 38px; height: 8px;
    background: var(--accent-aqua);
  }
  .front-footer-band {
    position: absolute; left: 0; right: 0; bottom: 0; height: 30px;
    background: var(--brand-blue);
  }

  .contact-block {
    position: absolute; left: 70px; top: 150px;
    color: var(--brand-blue);
  }
  .person-name {
    font-weight: 700; font-size: 42px; letter-spacing: 1px; line-height: 1;
    text-transform: uppercase;
  }
  .person-title {
    font-weight: 500; font-size: 19px; color: var(--ink-dark); margin-top: 6px;
  }
  .company-name {
    font-weight: 700; font-size: 29px; margin-top: 30px;
  }
  .contact-line {
    display: flex; align-items: center; gap: 14px;
    font-weight: 500; font-size: 25px; color: var(--ink-dark);
    margin-top: 10px;
  }
  .contact-line svg { width: 30px; height: 30px; flex: none; }

  .brand-mark {
    display: flex; align-items: center; gap: 16px;
    font-weight: 700; letter-spacing: 1px;
  }
  .brand-mark-front {
    position: absolute; right: 70px; top: 120px;
    color: var(--brand-blue); font-size: 40px;
  }
  .brand-mark-back { color: var(--card-white); font-size: 64px; gap: 24px; }
  .brand-dot { border-radius: 50%; flex: none; }
  .brand-mark-front .brand-dot { width: 44px; height: 44px; border: 6px solid var(--brand-blue); }
  .brand-mark-back .brand-dot { width: 72px; height: 72px; border: 9px solid var(--card-white); }
</style>
</head>
<body>
<main class="stage">
  <section class="card card-front" aria-label="Business card front">
    <div class="brand-mark brand-mark-front">
      <span class="brand-dot"></span>
      <span class="brand-name">Tarvik Works</span>
    </div>

    <div class="contact-block">
      <h1 class="person-name">Dana Whitlock</h1>
      <p class="person-title">President and Chief EMC Engineer</p>
      <p class="company-name">Tarvik Works, Inc.</p>
      <p class="contact-line">
        <svg viewBox="0 0 24 24" aria-hidden="true" fill="none" stroke="#2e4596" stroke-width="1.8">
          <circle cx="12" cy="12" r="10"/>
          <ellipse cx="12" cy="12" rx="4.5" ry="10"/>
          <line x1="2" y1="12" x2="22" y2="12"/>
          <line x1="4" y1="7" x2="20" y2="7"/>
          <line x1="4" y1="17" x2="20" y2="17"/>
        </svg>
        <span>www.tarvikworks.com</span>
      </p>
      <p class="contact-line">
        <svg viewBox="0 0 24 24" aria-hidden="true">
          <rect x="2" y="5" width="20" height="14" fill="#2e4596"/>
          <polyline points="2,5 12,13 22,5" fill="none" stroke="#ffffff" stroke-width="1.6"/>
        </svg>
        <span>dana@tarvikworks.com</span>
      </p>
    </div>

    <div class="front-footer-stripe"></div>
    <div class="front-footer-band"></div>
  </section>

  <section class="card card-back" aria-label="Business card back">
    <div class="brand-mark brand-mark-back">
      <span class="brand-dot"></span>
      <span class="brand-name">Tarvik Works</span>
    </div>
  </section>
</main>
</body>
</html>
```